Beef cattle farm needs signs which can be seen from roadside

We would like submissions of artwork for a sign that will hang from a fence or gate and will be seen by passing cars.

Existing logo and branding theme for the company is attached.

Signage can be between 900mm x 400mm - 1200mm x 600mm

Industry/Entity Type

Farm

Requirements
Must have
• the Signs should have the following information:
• Company name: Bellwin Grazing Company
• Address: 184 Tilbury Creek Road
• Contact number: 0491 362 815
• email address: admin@bellwingrazingco.example.com.au
• - Logo and branding as per attached artwork

```html
<!DOCTYPE html>
<html lang="en">
<head>
<meta charset="utf-8">
<title>Bellwin Grazing Company – Roadside Sign</title>
<link rel="stylesheet" href="https://fonts.googleapis.com/css2?family=Montserrat:wght@400;500&family=Arimo:wght@400;700&display=swap">
<style>
  :root {
    --backdrop: #8a8987;
    --green-top: #13603a;
    --green-bottom: #0a4223;
    --green-text: #176a35;
    --silver-light: #e4e5e7;
    --silver-dark: #a9abae;
    --panel-white: #ffffff;
    --panel-grey: #d9dadc;
    --ink: #1c1c1c;
    --white: #ffffff;
  }
  * { margin: 0; padding: 0; box-sizing: border-box; }
  html, body {
    width: 1200px;
    height: 655px;
    overflow: hidden;
    background: var(--backdrop);
  }
  .sign {
    position: absolute;
    left: 109px;
    top: 109px;
    width: 981px;
    height: 436px;
    background: linear-gradient(90deg, var(--panel-white) 45%, var(--panel-grey) 100%);
    overflow: hidden;
  }
  .sign__shapes {
    position: absolute;
    inset: 0;
  }
  .brand {
    position: absolute;
    left: 40px;
    width: 400px;
    text-align: center;
    color: var(--white);
    font-family: "Montserrat", sans-serif;
    font-weight: 500;
  }
  .brand__name {
    top: 282px;
    font-size: 62px;
    letter-spacing: 1px;
    line-height: 1;
  }
  .brand__tagline {
    top: 366px;
    font-size: 24px;
    letter-spacing: 0.5px;
    line-height: 1;
  }
  .contact {
    position: absolute;
    right: 33px;
    text-align: right;
    font-family: "Arimo", sans-serif;
    white-space: nowrap;
  }
  .contact__phone {
    top: 58px;
    font-size: 36px;
    font-weight: 700;
    color: var(--green-text);
  }
  .contact__address {
    top: 333px;
    font-size: 24px;
    font-weight: 400;
    color: var(--ink);
  }
  .contact__email {
    top: 373px;
    font-size: 18px;
    font-weight: 700;
    color: var(--ink);
  }
</style>
</head>
<body>
  <main class="sign">
    <svg class="sign__shapes" width="981" height="436" viewBox="0 0 981 436" aria-hidden="true">
      <defs>
        <linearGradient id="greenFill" x1="0" y1="0" x2="0" y2="1">
          <stop offset="0" stop-color="var(--green-top)"/>
          <stop offset="1" stop-color="var(--green-bottom)"/>
        </linearGradient>
        <linearGradient id="silverFill" x1="0" y1="0" x2="1" y2="0">
          <stop offset="0" stop-color="var(--silver-dark)"/>
          <stop offset="1" stop-color="var(--silver-light)"/>
        </linearGradient>
      </defs>
      <path class="sign__silver-band" d="M0,0 H464 Q620,218 474,436 H0 Z" fill="url(#silverFill)"/>
      <path class="sign__green-panel" d="M0,0 H441 Q598,218 450,436 H0 Z" fill="url(#greenFill)"/>
      <circle class="sign__brand-disc" cx="238" cy="158" r="116" fill="var(--white)"/>
    </svg>

    <div class="brand brand__name">BELLWIN</div>
    <div class="brand brand__tagline">GRAZING COMPANY</div>

    <div class="contact contact__phone">Call : 0491 362 815</div>
    <div class="contact contact__address">184 Tilbury Creek Road</div>
    <div class="contact contact__email">admin@bellwingrazingco.example.com.au</div>
  </main>
</body>
</html>
```